Blueberry Road side sign

I want a sign to put on the side of the road to advertise the that I have fresh local blueberries for sale. attatched is my company logo.
I want to use the same font that is used in my logo design.
I want "blueberries" written across the sign,
with maybe a couple of berries after the writing.

Industry/Entity Type

It Company

```html
<!DOCTYPE html>
<html lang="en">
<head>
<meta charset="utf-8">
<title>Blueberries Roadside Sign</title>
<link rel="stylesheet" href="https://fonts.googleapis.com/css2?family=Pacifico&family=Tinos:ital,wght@0,700;1,700&display=swap">
<style>
  :root {
    --canvas: #ffffff;
    --sign-edge: #3a3a3a;
    --sign-light: #f6f6f7;
    --sign-lavender: #c6c2dd;
    --sign-violet: #8a82bb;
    --sign-navy: #2c3891;
    --berry-blue: #0f57a8;
    --tag-white: #ffffff;
  }
  html, body {
    margin: 0;
    padding: 0;
    width: 1200px;
    height: 1000px;
    overflow: hidden;
    background: var(--canvas);
  }
  .canvas {
    position: relative;
    width: 1200px;
    height: 1000px;
  }
  .sign {
    position: absolute;
    left: 83px;
    top: 231px;
    width: 1032px;
    height: 516px;
    border: 1px solid var(--sign-edge);
    background: linear-gradient(156deg,
      var(--sign-light) 0%,
      #f2f2f4 42%,
      var(--sign-lavender) 63%,
      var(--sign-violet) 82%,
      var(--sign-navy) 100%);
    overflow: hidden;
  }
  .headline {
    position: absolute;
    left: 98px;
    top: 166px;
    margin: 0;
    font-family: "Pacifico", cursive;
    font-weight: 400;
    font-size: 122px;
    line-height: 1;
    color: var(--berry-blue);
    letter-spacing: -1px;
  }
  .berry-cluster {
    position: absolute;
    left: 712px;
    top: 176px;
    width: 226px;
    height: 170px;
    border-radius: 48% 52% 46% 54% / 50% 46% 54% 50%;
    background: radial-gradient(ellipse at 40% 40%, #8fa3d6 0%, #5b72b8 45%, #3b4f93 100%);
  }
  .brand {
    position: absolute;
    left: 56px;
    top: 374px;
    display: flex;
    align-items: center;
    gap: 22px;
  }
  .brand-dot {
    width: 86px;
    height: 86px;
    border-radius: 50%;
    background: var(--berry-blue);
  }
  .brand-text {
    display: flex;
    flex-direction: column;
    padding-top: 22px;
  }
  .brand-name {
    font-family: "Pacifico", cursive;
    font-weight: 400;
    font-size: 34px;
    line-height: 1.2;
    color: var(--berry-blue);
  }
  .brand-sub {
    font-family: "Tinos", "Times New Roman", serif;
    font-weight: 700;
    font-size: 9px;
    color: var(--berry-blue);
    padding-left: 2px;
  }
  .tagline {
    position: absolute;
    right: 82px;
    top: 455px;
    margin: 0;
    font-family: "Tinos", "Times New Roman", serif;
    font-style: italic;
    font-weight: 700;
    font-size: 24px;
    line-height: 1;
    color: var(--tag-white);
  }
</style>
</head>
<body>
  <main class="canvas">
    <section class="sign">
      <h1 class="headline">Blueberries</h1>
      <div class="berry-cluster" role="img" aria-label="Photo of a cluster of fresh blueberries with green leaves"></div>
      <div class="brand">
        <span class="brand-dot"></span>
        <span class="brand-text">
          <span class="brand-name">Hillside Farm</span>
          <span class="brand-sub">Hillside Blueberries</span>
        </span>
      </div>
      <p class="tagline">Fresh Local Blueberries</p>
    </section>
  </main>
</body>
</html>
```